Harbor LunaVital & Equipments

I need to create full stationery design for the company; Business Card, Envelop, Letterheads, Calendar and email template.

Our company is specialized in the import and export of nutritional, pharmaceutical and cosmetics in addition to medical equipments.

These is no limitation on how to use colors within the design.

Target Market(s)

Global

Industry/Entity Type

Healthcare

Other font styles liked:
• a font close to logo. Letterhead body text to be different than the address text

Requirements
Nice to have
• We will have multiple locations so it is good to keep space for future addresses.
• Stationary requirements:
• Letterhead: A4
• Envelopes: 3 regular sizes : large, medium and small (i do not know the sizes)
• Colors: extracted from the logo

```html
<!DOCTYPE html>
<html lang="en">
<head>
<meta charset="utf-8">
<title>Harbor LunaVital &amp; Equipments — Stationery</title>
<link href="https://fonts.googleapis.com/css2?family=Roboto:wght@400;500;700&family=Open+Sans:wght@400;700&display=swap" rel="stylesheet">
<style>
:root{
  --stage:#a3a3a3;
  --paper:#ffffff;
  --navy:#1e1b4f;
  --cyan:#29a9e0;
  --green:#2a9d3a;
  --orange:#f7a823;
  --ink:#222;
  --muted:#555;
  --faint:#e3e4ec;
}
*{box-sizing:border-box;margin:0;padding:0}
html,body{width:1200px;height:1200px;overflow:hidden}
body{background:var(--stage);font-family:'Roboto',sans-serif;color:var(--ink);position:relative}
.sheet{position:absolute;background:var(--paper);box-shadow:3px 4px 8px rgba(0,0,0,.35);overflow:hidden}
.card{width:349px;height:199px}
.card-1{left:51px;top:47px}
.card-2{left:428px;top:47px}
.card-3{left:806px;top:47px}
.card-4{left:51px;top:286px}
.card-5{left:428px;top:286px;background:var(--navy)}
.abs{position:absolute}

.brand{position:absolute;display:flex;flex-direction:column;align-items:center;text-align:center}
.brand-mark{background:var(--navy);border-radius:3px}
.brand-name{font-family:'Roboto',sans-serif;font-weight:700;color:var(--cyan);line-height:1.05}

.person-name{font-size:14.5px;font-weight:500;color:var(--navy)}
.person-role{font-size:9.5px;color:var(--muted);margin-top:2px}
.contact{font-size:11px;color:var(--muted);display:flex;align-items:center;gap:6px;white-space:nowrap}
.contact.dark{color:var(--ink);font-size:10.5px}
.icon{width:11px;height:11px;flex:none}
.address{font-size:10.5px;color:var(--ink);line-height:13px}

.rule-h{height:1px;background:var(--navy)}
.rule-v{width:1px}

.letterhead{left:142px;top:560px;width:406px;height:574px;box-shadow:6px 8px 12px rgba(0,0,0,.4)}
.lh-contact{left:308px;top:34px;font-size:5.2px;line-height:7.4px;color:var(--ink)}
.lh-contact div{display:flex;align-items:center;gap:3px}
.lh-contact svg{width:5px;height:5px}
.lh-heading{left:39px;top:93px;font-family:'Open Sans',sans-serif;font-weight:700;font-size:7px}
.lh-body{left:39px;width:326px;font-family:'Open Sans',sans-serif;font-size:6.4px;line-height:14.4px;color:#333}
.lh-sign-label{left:39px;top:406px;font-family:'Open Sans',sans-serif;font-size:6.5px}
.lh-signature{left:42px;top:416px;width:100px;height:30px;background:linear-gradient(90deg,#e8e8ea,#f4f4f5);border-radius:3px}
.lh-closing{left:39px;top:466px;font-family:'Open Sans',sans-serif;font-size:6.5px}
.faint-square{background:var(--faint);opacity:.85;border-radius:14px}

.envelope{width:454px;height:214px;box-shadow:8px 10px 12px rgba(0,0,0,.45)}
.env-front{left:581px;top:633px}
.env-back{left:581px;top:884px;width:451px;height:212px}
.env-address{left:18px;top:62px;font-size:4.8px;line-height:7px;color:#444}
</style>
</head>
<body>

<svg width="0" height="0" style="position:absolute">
  <defs>
    <symbol id="ico-mobile" viewBox="0 0 12 12"><circle cx="6" cy="6" r="6" fill="#1e1b4f"/><rect x="4" y="2.5" width="4" height="7" rx=".8" fill="#fff"/><rect x="4.8" y="3.4" width="2.4" height="4" fill="#1e1b4f"/></symbol>
    <symbol id="ico-phone" viewBox="0 0 12 12"><circle cx="6" cy="6" r="6" fill="#1e1b4f"/><path d="M3 5.2c0-1.2 1.4-1.8 3-1.8s3 .6 3 1.8l-1.2.3-.3-.8H4.5l-.3.8zM4.3 6h3.4l.8 2.6H3.5z" fill="#fff"/></symbol>
    <symbol id="ico-mail" viewBox="0 0 12 12"><circle cx="6" cy="6" r="6" fill="#1e1b4f"/><rect x="3" y="4" width="6" height="4.2" fill="#fff"/><path d="M3 4l3 2.4L9 4" stroke="#1e1b4f" stroke-width=".7" fill="none"/></symbol>
    <symbol id="ico-web" viewBox="0 0 12 12"><circle cx="6" cy="6" r="6" fill="#1e1b4f"/><circle cx="6" cy="6" r="3.2" fill="none" stroke="#fff" stroke-width=".7"/><path d="M2.8 6h6.4M6 2.8v6.4" stroke="#fff" stroke-width=".6"/><ellipse cx="6" cy="6" rx="1.4" ry="3.2" fill="none" stroke="#fff" stroke-width=".6"/></symbol>
    <symbol id="ico-pin" viewBox="0 0 12 12"><circle cx="6" cy="6" r="6" fill="#1e1b4f"/><path d="M6 2.6a2.2 2.2 0 0 1 2.2 2.2C8.2 6.5 6 9.2 6 9.2S3.8 6.5 3.8 4.8A2.2 2.2 0 0 1 6 2.6z" fill="#fff"/><circle cx="6" cy="4.8" r=".8" fill="#1e1b4f"/></symbol>
  </defs>
</svg>

<!-- Business card 1 -->
<section class="sheet card card-1">
  <div class="abs" style="left:25px;top:23px">
    <div class="person-name">Marcus Hale</div>
    <div class="person-role">Director</div>
  </div>
  <div class="abs rule-h" style="left:67px;top:49px;width:170px"></div>
  <div class="brand" style="left:246px;top:21px;width:82px">
    <div class="brand-mark" style="width:18px;height:18px"></div>
    <div class="brand-name" style="font-size:9px;margin-top:3px">Harbor LunaVital &amp; Equipments</div>
  </div>
  <div class="abs contact" style="left:22px;top:86px"><svg class="icon"><use href="#ico-mobile"/></svg>+0 414.662.3097</div>
  <div class="abs contact" style="left:22px;top:101px"><svg class="icon"><use href="#ico-phone"/></svg>+0 414.662.3097</div>
  <div class="abs contact" style="left:22px;top:121px"><svg class="icon"><use href="#ico-mail"/></svg>office.contact@mailhub.com</div>
  <div class="abs contact" style="left:22px;top:136px"><svg class="icon"><use href="#ico-web"/></svg>www.harborlunavital.com</div>
  <div class="abs address" style="left:22px;top:157px">7/208 Quayside addressline<br>PO BOX 4410, Area code</div>
</section>

<!-- Business card 2 -->
<section class="sheet card card-2">
  <div class="abs" style="left:28px;top:16px">
    <div class="person-name">Marcus Hale</div>
    <div class="person-role">Director</div>
  </div>
  <div class="brand" style="left:42px;top:124px;width:96px">
    <div class="brand-mark" style="width:22px;height:22px"></div>
    <div class="brand-name" style="font-size:10.5px;margin-top:4px">Harbor LunaVital &amp; Equipments</div>
  </div>
  <div class="abs rule-v" style="left:154px;top:113px;height:72px;background:var(--cyan)"></div>
  <div class="abs contact dark" style="left:168px;top:122px"><svg class="icon" style="width:8px;height:8px"><use href="#ico-mobile"/></svg>+0 414.662.3097</div>
  <div class="abs contact dark" style="left:168px;top:135px"><svg class="icon" style="width:8px;height:8px"><use href="#ico-phone"/></svg>+0 414.662.3097</div>
  <div class="abs contact dark" style="left:168px;top:154px"><svg class="icon" style="width:8px;height:8px"><use href="#ico-mail"/></svg>office.contact@mailhub.com</div>
  <div class="abs contact dark" style="left:168px;top:167px"><svg class="icon" style="width:8px;height:8px"><use href="#ico-web"/></svg>www.harborlunavital.com</div>
</section>

<!-- Business card 3 -->
<section class="sheet card card-3">
  <div class="brand" style="left:24px;top:105px;width:124px">
    <div class="brand-mark" style="width:30px;height:30px"></div>
    <div class="brand-name" style="font-size:13px;margin-top:5px">Harbor LunaVital &amp; Equipments</div>
  </div>
  <div class="abs rule-v" style="left:170px;top:21px;height:152px;background:var(--orange)"></div>
  <div class="abs" style="left:183px;top:23px">
    <div class="person-name">Marcus Hale</div>
    <div class="person-role">Director</div>
  </div>
  <div class="abs contact" style="left:183px;top:74px"><svg class="icon"><use href="#ico-mobile"/></svg>+0 414.662.3097</div>
  <div class="abs contact" style="left:183px;top:89px"><svg class="icon"><use href="#ico-phone"/></svg>+0 414.662.3097</div>
  <div class="abs contact" style="left:183px;top:109px"><svg class="icon"><use href="#ico-mail"/></svg>office.contact@mailhub.com</div>
  <div class="abs contact" style="left:183px;top:124px"><svg class="icon"><use href="#ico-web"/></svg>www.harborlunavital.com</div>
  <div class="abs address" style="left:183px;top:148px">7/208 Quayside addressline<br>PO BOX 4410, Area code</div>
</section>

<!-- Business card back, light -->
<section class="sheet card card-4">
  <div class="brand" style="left:0;top:42px;width:349px">
    <div class="brand-mark" style="width:60px;height:60px;border-radius:6px"></div>
    <div class="brand-name" style="font-size:27px;margin-top:10px">Harbor LunaVital<br>&amp; Equipments</div>
  </div>
</section>

<!-- Business card back, dark -->
<section class="sheet card card-5">
  <div class="brand" style="left:0;top:42px;width:349px">
    <div class="brand-mark" style="width:60px;height:60px;border-radius:6px;background:#fff"></div>
    <div class="brand-name" style="font-size:27px;margin-top:10px">Harbor LunaVital<br>&amp; Equipments</div>
  </div>
</section>

<!-- Letterhead -->
<section class="sheet letterhead">
  <div class="brand" style="left:39px;top:20px;width:102px">
    <div class="brand-mark" style="width:26px;height:26px"></div>
    <div class="brand-name" style="font-size:10.5px;margin-top:4px">Harbor LunaVital &amp; Equipments</div>
  </div>
  <div class="abs rule-v" style="left:294px;top:24px;height:48px;background:#444"></div>
  <div class="abs lh-contact">
    <div><svg><use href="#ico-phone"/></svg>000-417-2263</div>
    <div><svg><use href="#ico-mobile"/></svg>000-529-6481</div>
    <div><svg><use href="#ico-web"/></svg>www.lunavitalmail.com</div>
    <div><svg><use href="#ico-pin"/></svg>10482 Marlow Terrace</div>
    <div style="padding-left:8px">City Name, LA 63417</div>
  </div>
  <div class="abs lh-heading">Lorem Ipsum is simply</div>
  <p class="abs lh-body" style="top:125px">dummy text of the printing and typesetting industry. Lorem Ipsum has been the industry's standard dummy text ever since the 1500s, when an unknown printer took a galley of type and scrambled it to make a type specimen book. It has survived not only five centuries, but also the leap into electronic typesetting, remaining essentially unchanged. It was popularised in the 1960s with the release of Tranfex sheets containing Lorem Ipsum passages, and more recently with desktop publishing software like Quillset PageForm including versions of Lorem Ipsum.</p>
  <p class="abs lh-body" style="top:225px">It is a long established fact that a reader will be distracted by the readable content of a page when looking at its layout. The point of using Lorem Ipsum is that it has a more-or-less normal distribution of letters, as opposed to using 'Content here, content here', making it look like readable English. Many desktop publishing packages and web page editors now use Lorem Ipsum as their default model text, and a search for 'lorem ipsum' will uncover many web sites still in their infancy. Various versions have evolved over the years, sometimes by accident, sometimes on purpose (injected humour and the like).</p>
  <p class="abs lh-body" style="top:339px">Contrary to popular belief, Lorem Ipsum is not simply random text. It has roots in a piece of classical Latin literature from 45 BC, making it over 2000 years old. Daniel Whitcombe, a Latin professor at Alder Bay College in Maine, looked up one of the more obscure Latin words, consectetur, from a Lorem Ipsum passage.</p>
  <div class="abs lh-sign-label" style="top:411px">Lorem Ipsum</div>
  <div class="abs lh-signature" style="top:421px" role="img" aria-label="Handwritten signature"></div>
  <div class="abs lh-closing">Lorem Ipsum is a dummy</div>
  <div class="abs faint-square" style="left:262px;top:428px;width:170px;height:170px"></div>
</section>

<!-- Envelope front -->
<section class="sheet envelope env-front">
  <div class="brand" style="left:18px;top:14px;width:74px">
    <div class="brand-mark" style="width:20px;height:20px"></div>
    <div class="brand-name" style="font-size:8px;margin-top:3px">Harbor LunaVital &amp; Equipments</div>
  </div>
  <div class="abs env-address">9 Keswick House<br>Elmstead Business Village, City Name</div>
  <div class="abs faint-square" style="left:350px;top:110px;width:112px;height:112px"></div>
</section>

<!-- Envelope back -->
<section class="sheet envelope env-back">
  <svg class="abs" style="left:0;top:0" width="451" height="60" viewBox="0 0 451 60">
    <path d="M0 0 L46 46 Q51 51 58 51 L408 51 Q415 51 420 46 L451 14" fill="none" stroke="#4a4a8a" stroke-width=".8"/>
  </svg>
  <div class="abs brand-mark" style="left:209px;top:9px;width:34px;height:34px;border-radius:4px"></div>
</section>

</body>
</html>
```